Bold, Modern, Clean "Vernatouchmassage.com" website

Why we stand out?
We are a male and female mobile massage team. Our names are Jonah and Tessa. 
Verna Touch is a Seattle based mobile massage service. Our massage is offered to the community with a goal of facilitating balance within each individual. We specialize in integrated Pain management, and sports/medical massage therapy. Every client's first assessment is attended by our male and female massage therapist team. Depending on the goals identified for an individual determines which therapist will be assigned to provide treatment, if not both.

Our passion...
Here at Verna Touch, we have a great passion for Postural Resoration and how it is integrated into an individual's Massage treatment. We pride ourselves in being natural facilitators of healing, which takes the ego of the therapist out of the client's healing process. We strive to deliver the best massage possible by including modalities such as Neuromuscular, Myofascial release, spontaneous muscle release, postural restoration, orthopedic, and medical massage.

Our education...

We are both Graduates of Alvenra, school of massage therapy. We have continuing education in medical massage, myofacial release, trigger point therapy, postural restoration, anatomy, and spontaneous muscle release. Tessa is also a Certified Yoga Instructor, which amplifies her experience with flexibility and strength as it pertains to each individual. Jonah's passion is Massage, stretching, and strength training to encourage postural restoration and realignment.

Our rates-

Our rates are $75/ 60 minutes, $95/ 90 minutes, and $120/ 120 minutes.

Education-
Both Tessa and I worked as behavioral health professionals that specialized in life skills mentoring for youth who had experienced different types of trauma. This led us both to want to help others in a different environment, where individuals can be empowered to take responsibility over their own healing. To us, massage is a type of manipulation physical therapy, that encourages healing on many levels.

Advice to any massage client-
The most important thing to 'us', as Licenced providers is to get you on to our table to show you our skills. But a good therapist never forgets that it's not about what we do for you, but what we can facilitate for you. Your health and healing has nothing to do with us. It is yours, not ours. Identify what your goals are with any Therapist, and know what the end looks like. Progress should be tangible, such as range of motion, and decreased pain.

5/5 stars Massage Therapy
Verified Review

Tessa and Jonah at Verna Touch are awesome! I recently had open heart surgery, and Tessa worked on me to increase my range of motion while helping with the pinched nerve from my arm being in the same position for so long during my surgery. My wife drives a lot for work, and Jonah has helped decrease her neck and lower back pain immensely. They are seriously the best therapists I have ever worked with. I would recommend them to anyone who needs anything from stress relief to a medical massage treatment. They are professional, up beat, easy going, and always on time. And, I love that they meet us where ever we like! We did a staycation recently, where they came to our hotel to give us relaxation massages. Although usually they come to our home, where we focus on pain related issues. We will continue to work with them for a long, long time.

Brisa K. on December 17, 2015

Target Market(s)

Mobile massage therapy clients

Industry/Entity Type

Massage Therapy

Coding

Coded - Design and coding required

Number of Pages Required

1 page

Font styles to use
Serif
Sans Serif

Requirements
Must have
• Please add or remove any information that would help the presentation of our website. Our logo is posted below, please include into the website.
• Please include a contact field that includes, vernatouchmassage@quillmail.test,
• (206) 555-0147
• We have also included our own stock photos, as well as a photo of Jonah and Tessa. Please include a cropped photo of both massage therapists.

```html
<!DOCTYPE html>
<html lang="en">
<head>
<meta charset="utf-8">
<title>Verna Touch – Mobile Massage</title>
<link href="https://fonts.googleapis.com/css2?family=Open+Sans:wght@400;600;700;800&family=Oswald:wght@400;500&display=swap" rel="stylesheet">
<style>
:root{
  --navy:#1d2a6e;
  --blue:#0a8ac4;
  --blue-dark:#135aa8;
  --price-a:#1a4fa3;
  --price-b:#0f6fbe;
  --footer:#1570b9;
  --panel:#f1f1f1;
  --text:#555;
  --muted:#888;
  --white:#fff;
}
*{box-sizing:border-box;margin:0;padding:0}
html,body{width:667px;height:1200px;overflow:hidden;background:var(--white)}
body{font-family:"Open Sans",Arial,sans-serif;color:var(--text)}
.page{position:relative;width:667px;height:1200px;overflow:hidden}
.abs{position:absolute}

/* header */
.top-rule{left:0;top:0;width:667px;height:2px;background:var(--blue)}
.nav{left:0;top:37px;width:667px;height:14px}
.nav a{position:absolute;font-size:6.2px;font-weight:600;color:#666;text-decoration:none;letter-spacing:.2px;white-space:nowrap}
.nav a.active{color:var(--navy)}
.nav a.active::after{content:"";position:absolute;left:0;right:0;top:11px;height:1.5px;background:var(--navy)}
.brand-mark{border-radius:50%;background:var(--navy);display:flex;flex-direction:column;align-items:center;justify-content:center;color:var(--white);font-weight:800;text-align:center;line-height:1}
.header-brand{left:298px;top:6px;width:72px;height:72px;border:2px solid #fff;box-shadow:0 0 0 1.5px var(--navy);font-size:12px;z-index:3}
.call-badge{left:458px;top:0;width:118px;height:28px;background:var(--blue);border-radius:0 0 60px 60px/0 0 22px 22px;color:var(--white)}
.call-badge svg{position:absolute;left:19px;top:8px}
.call-badge .label{position:absolute;left:46px;top:4px;font-size:5px;font-weight:700;letter-spacing:.3px}
.call-badge .num{position:absolute;left:46px;top:10px;font-family:Oswald,sans-serif;font-size:9.5px}

/* hero */
.hero{left:0;top:56px;width:667px;height:226px;background:
  radial-gradient(ellipse 90px 60px at 56% 50%,rgba(30,30,30,.55),transparent 70%),
  linear-gradient(100deg,#e3c39f 0%,#c98f6d 25%,#b8785a 45%,#d9a887 62%,#e7cfb0 100%)}
.quick{left:458px;top:90px;width:120px;height:172px;background:rgba(40,50,110,.88);padding:10px 10px 0}
.quick h3{color:var(--white);font-size:7px;font-weight:700;letter-spacing:1px;text-align:center;margin:1px 0 10px}
.field{height:15px;background:var(--white);margin-bottom:4px;font-size:5px;color:#555;display:flex;align-items:center;padding-left:6px;gap:5px}
.field.msg{height:46px;align-items:flex-start;padding-top:5px}
.quick .submit{height:21px;background:var(--blue);color:var(--white);font-size:7.5px;font-weight:700;letter-spacing:1px;display:flex;align-items:center;justify-content:center;margin-top:5px}
.dot{top:263px;width:7px;height:7px;border-radius:50%;background:var(--white)}
.dot.on{background:transparent;border:1.3px solid var(--white)}

/* massages */
.section-title{color:var(--navy);font-weight:800;letter-spacing:1.2px;text-align:center}
.massages-title{left:0;top:292px;width:667px;font-size:10.5px}
.massages-sub{left:0;top:307px;width:667px;text-align:center;font-size:6.5px;color:#666}
.card{top:325px;width:158px}
.card .photo{height:85px}
.card h4{font-size:8px;font-weight:400;color:var(--navy);text-align:center;margin-top:6px}
.btn{display:block;background:var(--blue);color:var(--white);font-size:5px;font-weight:700;letter-spacing:.8px;text-align:center}
.card .btn{width:48px;height:9px;line-height:9px;margin:4px auto 0}

/* why / how */
.why{left:90px;top:452px;width:256px;height:223px;background:linear-gradient(135deg,#9aa6b0 0%,#d9d2c8 45%,#b8a597 100%)}
.why-ring{left:36px;top:19px;width:184px;height:184px;border-radius:50%;border:2px solid rgba(255,255,255,.9)}
.why-disc{left:42px;top:25px;width:172px;height:172px;border-radius:50%;background:rgba(255,255,255,.86);text-align:center;padding:0 22px}
.why-disc .brand-mark{width:30px;height:30px;margin:12px auto 8px;font-size:5px}
.why-disc h3{font-size:8.5px;font-weight:600;letter-spacing:1px;color:#333;line-height:1.2}
.why-disc p{font-size:5.2px;line-height:1.75;color:#444;margin-top:6px}
.why-disc .btn{width:54px;height:12px;line-height:12px;margin:6px auto 0}
.how{left:346px;top:452px;width:232px;height:223px;background:var(--panel)}
.how-head{left:0;top:29px;width:232px;font-size:8px}
.how-head span{position:absolute;top:0}
.how .brand-mark{left:93px;top:8px;width:44px;height:44px;border:1.5px solid #fff;box-shadow:0 0 0 1px var(--navy);font-size:7.5px}
.step-card{left:54px;width:168px;height:42px;background:var(--white);box-shadow:0 1px 2px rgba(0,0,0,.08);padding:6px 6px 0 19px}
.step-card h5{font-size:7px;font-weight:400;color:var(--navy)}
.step-card p{font-size:5px;line-height:1.55;color:#777;margin-top:3px}
.step-dot{left:9px;width:48px;height:48px;border-radius:50%;background:var(--blue);color:var(--white);text-align:center}
.step-dot b{display:block;font-size:5px;letter-spacing:.8px;margin-top:12px}
.step-dot svg{margin-top:3px}

/* pricing */
.pricing{left:90px;top:682px;width:488px;height:184px;background:radial-gradient(ellipse at 30% 20%,var(--price-b),var(--price-a) 70%)}
.pricing-title{left:0;top:14px;width:488px;color:var(--white);font-size:10px;font-weight:700;letter-spacing:1.5px;text-align:center}
.price{top:50px;width:124px;height:124px;border-radius:50%;border:2px solid rgba(255,255,255,.22);padding:4px}
.price-inner{width:112px;height:112px;border-radius:50%;background:rgba(10,120,200,.45);color:var(--white);text-align:center;position:relative}
.price .mins{font-family:Oswald,sans-serif;font-size:27px;line-height:1;padding-top:14px}
.price .lbl{font-size:8px;font-weight:600;letter-spacing:1.5px}
.price hr{border:0;border-top:1px solid rgba(255,255,255,.3);margin:7px 0 6px}
.price .from{font-size:7.5px;font-weight:600;letter-spacing:1px}
.price .amt{font-family:Oswald,sans-serif;font-size:20px;line-height:1.1}

/* testimonials */
.reviews{left:90px;top:875px;width:488px;height:161px;background:var(--panel);border:1px solid #e4e4e4}
.reviews-title{left:0;top:13px;width:488px;font-size:8.5px}
.reviews-title svg{vertical-align:middle;margin:0 9px}
.reviews-rule{left:194px;top:28px;width:100px;height:1px;background:#ccc}
.divider{left:243px;top:42px;width:1px;height:108px;background:#ddd}
.avatar{top:48px;width:38px;height:38px;border-radius:50%;border:2px solid var(--white);box-shadow:0 0 0 1px #ccc;background:linear-gradient(#c9ced6,#8f98a6)}
.quote-mark{font-size:26px;color:#ddd;font-weight:800;top:78px;font-family:Georgia,serif;line-height:1}
.review-text{top:93px;width:192px;font-size:5.6px;line-height:1.75;color:#666;text-align:center}
.review-name{top:133px;width:192px;font-size:5.3px;text-align:center;color:#666}
.review-name b{color:var(--blue);letter-spacing:.6px}

/* footer */
.footer{left:0;top:1048px;width:667px;height:152px;background:radial-gradient(ellipse at 60% 30%,#1b85c9,var(--footer) 60%,#0f5ea8)}
.foot-h{top:21px;color:var(--white);font-size:7.5px;font-weight:700;letter-spacing:1px}
.foot-list{top:38px;list-style:none;color:var(--white);font-size:5.3px;letter-spacing:.6px;line-height:10.8px}
.foot-contact{top:38px;width:140px;color:var(--white);font-size:5.3px;letter-spacing:.5px;line-height:10px}
.foot-contact p+p{margin-top:8px}
.foot-input{left:342px;width:102px;height:18px;background:var(--white);font-size:5px;font-weight:700;letter-spacing:.6px;color:#555;padding:6px 0 0 7px}
.foot-btn{left:342px;top:78px;width:102px;height:18px;background:var(--blue);color:var(--white);font-size:6px;font-weight:700;letter-spacing:.8px;text-align:center;line-height:18px}
.footer .brand-mark{left:508px;top:16px;width:68px;height:68px;background:#1d3a8c;border:1.5px solid rgba(255,255,255,.5);font-size:11px}
.foot-rule{left:90px;top:115px;width:488px;height:1px;background:rgba(255,255,255,.25)}
.follow{left:90px;top:131px;color:var(--white);font-size:5px;letter-spacing:.8px}
.social{top:127px;width:15px;height:15px;border-radius:50%}
.copy{right:89px;top:131px;color:var(--white);font-size:5px;letter-spacing:.8px}
</style>
</head>
<body>
<div class="page">

  <div class="abs top-rule"></div>

  <nav class="abs nav">
    <a class="active" style="left:158px">HOME</a>
    <a style="left:193px">ABOUT US</a>
    <a style="left:239px">HOW IT WORKS</a>
    <a style="left:378px">MASSAGES</a>
    <a style="left:427px">TESTIMONIALS</a>
    <a style="left:487px">CONTACT US</a>
  </nav>

  <div class="abs brand-mark header-brand">VERNA<br>TOUCH</div>

  <div class="abs call-badge">
    <svg width="10" height="10" viewBox="0 0 10 10"><circle cx="5" cy="5" r="5" fill="#1d2a6e"/><path d="M3.3 2.6l1 .9-.5.7c.4.8 1 1.4 1.8 1.8l.7-.5.9 1-.7.8C4.8 7.1 2.9 5.2 2.5 3.3z" fill="#fff"/></svg>
    <span class="label">CALL US ON :</span>
    <span class="num">(206) 555-0147</span>
  </div>

  <div class="abs hero" role="img" aria-label="Photo of a woman receiving a hot stone back massage"></div>

  <form class="abs quick">
    <h3>QUICK CONTACT</h3>
    <div class="field"><svg width="5" height="5" viewBox="0 0 10 10"><circle cx="5" cy="3" r="2.6" fill="#333"/><path d="M0 10c0-3 2.2-4.5 5-4.5S10 7 10 10z" fill="#333"/></svg>Name</div>
    <div class="field"><svg width="6" height="5" viewBox="0 0 12 9"><rect x=".5" y=".5" width="11" height="8" fill="none" stroke="#333"/><path d="M.5.5l5.5 4.5L11.5.5" fill="none" stroke="#333"/></svg>E mail</div>
    <div class="field"><svg width="5" height="5" viewBox="0 0 10 10"><path d="M1.6 .8l2 1.8-1 1.4c.8 1.6 2 2.8 3.6 3.6l1.4-1 1.8 2-1.4 1.6C4.2 9.2.8 5.8.4 2.2z" fill="#333"/></svg>Phone</div>
    <div class="field msg"><svg width="5" height="5" viewBox="0 0 10 10"><rect x=".5" y="1.5" width="8" height="8" fill="none" stroke="#333"/><path d="M4 6l5-5.5" stroke="#333" stroke-width="1.4"/></svg>Message</div>
    <div class="submit">SUBMIT</div>
  </form>

  <span class="abs dot" style="left:295px"></span>
  <span class="abs dot on" style="left:312px"></span>
  <span class="abs dot" style="left:330px"></span>
  <span class="abs dot" style="left:349px"></span>
  <span class="abs dot" style="left:366px"></span>

  <h2 class="abs section-title massages-title">MASSAGES</h2>
  <p class="abs massages-sub">We are a male and female mobile massage team.</p>

  <div class="abs card" style="left:90px">
    <div class="photo" role="img" aria-label="Photo of a stressed office worker holding his head at his desk" style="background:linear-gradient(135deg,#e4e5e8,#9da0a6 45%,#2d2f36 60%,#c7c9cc)"></div>
    <h4>Pain Management</h4><span class="btn">READ MORE</span>
  </div>
  <div class="abs card" style="left:254px">
    <div class="photo" role="img" aria-label="Photo of a therapist stretching an athlete's leg" style="background:linear-gradient(135deg,#efe9e4,#d2a488 40%,#e27a3a 55%,#3b4a6b 70%,#e9e3de)"></div>
    <h4>Sports Massage Therapy</h4><span class="btn">READ MORE</span>
  </div>
  <div class="abs card" style="left:418px">
    <div class="photo" role="img" aria-label="Photo of a man receiving a back massage" style="background:linear-gradient(135deg,#c0703c,#a8664c 40%,#e2b49c 60%,#f1ece8)"></div>
    <h4>Medical Massage</h4><span class="btn">READ MORE</span>
  </div>

  <section class="abs why" role="img" aria-label="Photo of a relaxed woman at a spa">
    <div class="abs why-ring"></div>
    <div class="abs why-disc">
      <div class="brand-mark">VERNA<br>TOUCH</div>
      <h3>WHY WE<br>STAND OUT?</h3>
      <p>We are a male and female mobile massage team. Our names are Jonah and Tessa. Verna Touch is a Seattle based mobile massage service. Our massage is offered to the community with a goal of facilitating balance within each individual.</p>
      <span class="btn">READ MORE</span>
    </div>
  </section>

  <section class="abs how">
    <h2 class="abs section-title how-head"><span style="left:66px">HOW</span><span style="left:142px">WORKS</span></h2>
    <div class="abs brand-mark">VERNA<br>TOUCH</div>

    <div class="abs step-card" style="top:61px"><h5>Book Massage</h5><p>Here at Verna Touch, we have a great passion for Postural Resoration.</p></div>
    <div class="abs step-dot" style="top:60px"><b>STEP 1</b>
      <svg width="13" height="13" viewBox="0 0 14 14"><rect x="1" y="3" width="10" height="10" rx="1.5" fill="none" stroke="#fff" stroke-width="1.3"/><path d="M5 9l1-3 6-6 2 2-6 6z" fill="none" stroke="#fff" stroke-width="1.2"/></svg></div>

    <div class="abs step-card" style="top:114px"><h5>Confirm Your Appointment</h5><p>Here at Verna Touch, we have a great passion for Postural Resoration and how it is integrated .</p></div>
    <div class="abs step-dot" style="top:112px"><b>STEP 2</b>
      <svg width="13" height="13" viewBox="0 0 14 14"><rect x="1" y="2" width="12" height="11" fill="none" stroke="#fff" stroke-width="1.3"/><path d="M1 5h12M4 0v3M10 0v3M4 7v4M7 7v4M10 7v4M2 8h10M2 10.5h10" stroke="#fff" stroke-width="1"/></svg></div>

    <div class="abs step-card" style="top:166px"><h5>Finishing</h5><p>We are both Graduates of Alvenra, school of massage therapy.</p></div>
    <div class="abs step-dot" style="top:165px"><b>STEP 3</b>
      <svg width="13" height="13" viewBox="0 0 14 14"><path d="M1.5 7.5l3.5 3.5 7.5-8" fill="none" stroke="#fff" stroke-width="2.2"/></svg></div>
  </section>

  <section class="abs pricing">
    <h2 class="abs pricing-title">PRICING</h2>
    <div class="abs price" style="left:33px"><div class="price-inner"><div class="mins">60</div><div class="lbl">MINUTES</div><hr><div class="from">FROM</div><div class="amt">$75</div></div></div>
    <div class="abs price" style="left:182px"><div class="price-inner"><div class="mins">90</div><div class="lbl">MINUTES</div><hr><div class="from">FROM</div><div class="amt">$95</div></div></div>
    <div class="abs price" style="left:330px"><div class="price-inner"><div class="mins">120</div><div class="lbl">MINUTES</div><hr><div class="from">FROM</div><div class="amt">$120</div></div></div>
  </section>

  <section class="abs reviews">
    <h2 class="abs section-title reviews-title">
      <svg width="7" height="8" viewBox="0 0 7 8"><path d="M7 0v8L0 4z" fill="#1d2a6e"/></svg>WHAT CUSTOMERS SAY ABOUT &nbsp;US?<svg width="7" height="8" viewBox="0 0 7 8"><path d="M0 0v8l7-4z" fill="#1d2a6e"/></svg>
    </h2>
    <div class="abs reviews-rule"></div>
    <div class="abs divider"></div>

    <div class="abs avatar" style="left:106px" role="img" aria-label="Portrait of the reviewer"></div>
    <span class="abs quote-mark" style="left:24px">“</span>
    <p class="abs review-text" style="left:26px">Tessa and Jonah at Verna Touch are awesome! I recently had open heart surgery, and Tessa worked on me to increase my range &nbsp;of motion while helping....</p>
    <p class="abs review-name" style="left:26px"><b>DORIAN VELASCO,</b> England</p>

    <div class="abs avatar" style="left:350px" role="img" aria-label="Portrait of the reviewer"></div>
    <span class="abs quote-mark" style="left:264px">“</span>
    <p class="abs review-text" style="left:270px">The most important thing to 'us', as Licenced providers is to get you on to our table to show you our skills. But a good therapist never forgets that it's not about what we do for you...</p>
    <p class="abs review-name" style="left:270px"><b>DORIAN VELASCO,</b> England</p>
  </section>

  <footer class="abs footer">
    <h4 class="abs foot-h" style="left:90px">MENU</h4>
    <ul class="abs foot-list" style="left:90px">
      <li>HOME</li><li>ABOUT US</li><li>HOW IT WORKS</li><li>MASSAGES</li><li>TESTIMONIALS</li><li>CONTACT US</li>
    </ul>

    <h4 class="abs foot-h" style="left:193px">CONTACT US</h4>
    <div class="abs foot-contact" style="left:193px">
      <p>418 MARROW LANE, TACOMA,<br>WA 98402</p>
      <p>1.800.555.0123</p>
      <p>VERNATOUCHMASSAGE@QUILLMAIL.TEST</p>
    </div>

    <h4 class="abs foot-h" style="left:342px">NEWSLETTER SIGNUP!</h4>
    <div class="abs foot-input" style="top:34px">NAME</div>
    <div class="abs foot-input" style="top:56px">E MAIL</div>
    <div class="abs foot-btn">SIGNUP!</div>

    <div class="abs brand-mark">VERNA<br>TOUCH</div>

    <div class="abs foot-rule"></div>
    <span class="abs follow">FOLLOW US ON</span>
    <span class="abs social" style="left:142px;background:#3b5bb5"></span>
    <span class="abs social" style="left:160px;background:#2aa4e6"></span>
    <span class="abs social" style="left:178px;background:#e1522f"></span>
    <span class="abs copy">COPYRIGHTS @ 2015 ALL RIGHTS RESERVED</span>
  </footer>

</div>
</body>
</html>
```